Website for company called VORENTbio

We need a website for our new company called VORENTbio which developed a platform/technology to identify antigen-specific T cells (immune cells) which can be used for cancer therapy, autoimmunity, etc.

The platform is called VORENT and is rapid, versatile, unbiased, and inexpensive.

We have a semi-final logo although we are not completely set on color and font of text (attached).

Target Market(s)

Our target audience at the moment would be potential investors and VCs. We eventually are interested in getting attention from scientists and cell/immunotherapy companies.

Industry/Entity Type

Healthcare/Technology

Coding

Coded - Design and coding required

Number of Pages Required

1 page

Colors
0094D4
00A9DD
6FCCEA
C7EBF8
E9F6FB
00AB8E
00BBA5
67D7C9
C6EFE9
E9F9F6
E54698
E96AAD
F1A4CE
F9D9EA
FCEFF6
A7469A
B969AE
D3A5CF
EDDBEB
F8F0F9
6B429C
8869AF
B7A5CE
E3DAEB
F3F0F8

Requirements
Must have
• Landing page about the company, About us page, Technology page (could be merged with company landing page), Contact us page

```html
<!DOCTYPE html>
<html lang="en">
<head>
<meta charset="utf-8">
<title>VORENTbio — Antigen-Specific T Cell Discovery</title>
<link href="https://fonts.googleapis.com/css2?family=Poppins:wght@400;500;600;700;800&display=swap" rel="stylesheet">
<style>
:root{
  --navy:#1b1448;
  --navy-deep:#130e36;
  --violet:#6B429C;
  --violet-soft:#8869AF;
  --plum:#A7469A;
  --pink:#E54698;
  --pink-soft:#F9D9EA;
  --lilac:#F3F0F8;
  --lilac-2:#E3DAEB;
  --blue:#0094D4;
  --teal:#00AB8E;
  --ink:#1d1a33;
  --muted:#6a6680;
  --white:#ffffff;
  --grad:linear-gradient(90deg,var(--pink),var(--violet));
}
*{box-sizing:border-box;margin:0;padding:0}
html,body{width:1200px;height:3200px;overflow:hidden}
body{font-family:"Poppins",sans-serif;color:var(--ink);background:var(--white);position:relative}
a{color:inherit;text-decoration:none}
.btn{display:inline-flex;align-items:center;justify-content:center;height:40px;padding:0 22px;border-radius:6px;font-size:12px;font-weight:600}
.btn-grad{background:var(--grad);color:#fff}
.btn-ghost{border:1px solid rgba(255,255,255,.6);color:#fff}
.btn-dark{background:var(--navy);color:#fff}
.photo{display:block}

/* dark top */
.top{position:absolute;left:0;top:0;width:1200px;height:1000px;background:linear-gradient(160deg,#241a5e 0%,var(--navy) 45%,var(--navy-deep) 100%);overflow:hidden}
.nav{position:absolute;top:18px;left:60px;right:60px;display:flex;align-items:center;justify-content:space-between;z-index:3}
.brand{display:flex;align-items:center;gap:8px;font-weight:700;font-size:22px;color:#fff}
.brand-dot{width:22px;height:22px;border-radius:50%;background:var(--pink)}
.nav-links{display:flex;gap:26px;align-items:center;font-size:12px;color:#fff}
.nav-links .btn{height:32px;padding:0 16px;font-size:11px}
.hero-title{position:absolute;left:60px;top:115px;width:560px;font-size:56px;line-height:1.08;font-weight:800;color:#fff}
.hero-text{position:absolute;left:60px;top:310px;width:440px;font-size:13px;line-height:1.6;color:#d8d3ea}
.hero-actions{position:absolute;left:60px;top:368px;display:flex;gap:14px}
.hero-photo{position:absolute;left:720px;top:0;width:420px;height:540px;background:linear-gradient(180deg,#6a5fa4,#3a2f78);border-radius:0 0 0 200px}
.audience{position:absolute;left:60px;top:450px;display:flex;gap:16px}
.audience-card{width:230px;height:90px;border-radius:10px;background:rgba(255,255,255,.1);border:1px solid rgba(255,255,255,.18);display:flex;align-items:center;justify-content:space-between;padding:0 14px 0 18px;color:#fff;font-size:14px;font-weight:600;line-height:1.3}
.audience-card .photo{width:64px;height:78px;border-radius:8px;background:linear-gradient(180deg,#b9b0d8,#7d6fb3);align-self:flex-end}
.what-photo{position:absolute;left:140px;top:590px;width:380px;height:380px;border-radius:50%;background:radial-gradient(circle at 40% 40%,#c9c0e3,#7a6bb0);border:8px solid rgba(255,255,255,.12)}
.what{position:absolute;left:680px;top:650px;width:440px;color:#fff}
.what h2{font-size:36px;font-weight:700;margin-bottom:14px}
.what p{font-size:12.5px;line-height:1.65;color:#d8d3ea;margin-bottom:12px}
.what .btn{height:34px;font-size:11px;margin-top:6px}

/* advantage */
.section-title{text-align:center;font-size:32px;font-weight:700;color:var(--ink)}
.advantage{position:absolute;top:1020px;left:0;width:1200px}
.adv-grid{display:flex;gap:16px;justify-content:center;margin-top:36px}
.adv-card{width:258px;height:96px;background:#fff;border:1px solid var(--lilac-2);border-radius:10px;box-shadow:0 6px 18px rgba(107,66,156,.1);display:flex;gap:12px;padding:16px}
.adv-icon{width:40px;height:40px;border-radius:50%;background:var(--lilac);flex:none;display:flex;align-items:center;justify-content:center}
.adv-card h3{font-size:14px;font-weight:700}
.adv-card p{font-size:10.5px;color:var(--muted);line-height:1.4;margin-top:2px}
.adv-card .more{font-size:10px;color:var(--pink);font-weight:600;margin-top:4px;display:block}
.center-btn{display:flex;justify-content:center;margin-top:36px}
.center-btn .btn{height:34px;font-size:11px}

/* future */
.future{position:absolute;top:1350px;left:0;width:1200px}
.future-grid{display:flex;gap:24px;justify-content:center;margin-top:34px}
.future-card{width:340px}
.future-card .photo{height:200px;border-radius:10px;background:linear-gradient(135deg,#d7e6f1,#8fb2cf)}
.future-card h3{font-size:17px;font-weight:700;margin-top:16px}
.future-card p{font-size:11px;color:var(--muted);margin-top:4px;line-height:1.5}

/* built */
.built{position:absolute;top:1900px;left:0;width:1200px;height:380px;background:linear-gradient(120deg,var(--navy-deep),#2a1f66)}
.built-text{position:absolute;left:110px;top:50px;width:500px;color:#fff}
.built-text h2{font-size:38px;line-height:1.15;font-weight:800}
.built-text p{font-size:12.5px;line-height:1.65;color:#d8d3ea;margin-top:16px}
.built-actions{display:flex;gap:14px;margin-top:26px}
.built-photo{position:absolute;left:700px;top:-40px;width:390px;height:390px;border-radius:50%;background:radial-gradient(circle at 45% 40%,#e5dbe6,#9b8fc0);border:10px solid #fff;box-shadow:0 10px 30px rgba(0,0,0,.25)}

/* reviews */
.reviews{position:absolute;top:2370px;left:0;width:1200px}
.review-grid{display:flex;gap:70px;justify-content:center;margin-top:34px}
.review{width:420px;border-left:2px solid var(--lilac-2);padding-left:22px}
.quote{width:30px;height:23px}
.review blockquote{font-size:15px;line-height:1.5;font-weight:600;color:var(--ink);margin-top:10px}
.reviewer{display:flex;align-items:center;gap:12px;margin-top:14px;font-size:13px}
.reviewer .photo{width:40px;height:40px;border-radius:50%;background:linear-gradient(135deg,#cfc4e4,#8b7bbb)}
.stars{color:#f5b301;font-size:11px;letter-spacing:1px}
.reviewer span{display:block;font-size:10px;color:var(--muted)}

/* contact band */
.talk{position:absolute;top:2700px;left:110px;width:980px;height:250px;border-radius:16px;background:linear-gradient(100deg,#3d2c94,var(--violet) 55%,#5a3fc0);overflow:hidden}
.talk-photo{position:absolute;left:90px;top:10px;width:380px;height:240px;background:linear-gradient(180deg,#b8b0da,#6f5fb0);border-radius:12px 12px 0 0}
.talk-text{position:absolute;left:580px;top:50px;width:340px;color:#fff}
.talk-text h2{font-size:36px;font-weight:700}
.talk-text p{font-size:11.5px;line-height:1.6;color:#e4def3;margin-top:8px}
.talk-text .btn{height:32px;font-size:11px;margin-top:18px}

/* footer */
.footer{position:absolute;top:2990px;left:0;width:1200px;height:210px;background:var(--navy-deep);color:#cfc9e4}
.footer-cols{display:flex;gap:40px;padding:30px 60px 0}
.footer-about{width:250px;font-size:10.5px;line-height:1.55}
.footer-about .brand{margin-bottom:12px}
.footer-col h4{color:#fff;font-size:13px;font-weight:600;margin-bottom:8px}
.footer-col li{list-style:none;font-size:10.5px;line-height:1.4;margin-bottom:3px;display:flex;align-items:center;gap:6px}
.icon-sq{width:12px;height:12px;border-radius:3px;background:var(--violet-soft);display:inline-block}
.news{width:250px}
.news-form{display:flex;margin-top:4px}
.news-form span{flex:1;height:30px;border-radius:5px 0 0 5px;background:#fff;font-size:10px;color:#999;padding:8px 10px}
.news-form b{height:30px;padding:0 14px;border-radius:0 5px 5px 0;background:var(--grad);color:#fff;font-size:10px;display:flex;align-items:center}
.footer-bar{position:absolute;left:60px;right:60px;bottom:12px;border-top:1px solid rgba(255,255,255,.12);padding-top:10px;display:flex;justify-content:space-between;font-size:10px}
.footer-bar nav{display:flex;gap:20px}
</style>
</head>
<body>

<section class="top">
  <header class="nav">
    <a class="brand" href="#"><span class="brand-dot"></span>vorentbio</a>
    <nav class="nav-links">
      <a href="#">Home</a><a href="#">About Us</a><a href="#">Studies</a><a href="#">Advantage</a><a href="#">Investors</a>
      <a class="btn btn-grad" href="#">Contact Us</a>
    </nav>
  </header>

  <h1 class="hero-title">Unlocking the Power of Antige -Specific T Cells</h1>
  <p class="hero-text">VORENTbio is pioneering a new platform to rapidly and precisely identify the T cells that drive effective immunotherapy.</p>
  <div class="hero-actions">
    <a class="btn btn-grad" href="#">Download Investor Brief</a>
    <a class="btn btn-ghost" href="#">Contact the Team</a>
  </div>
  <div class="photo hero-photo" role="img" aria-label="Smiling doctor in a white coat holding a folder"></div>

  <div class="audience">
    <div class="audience-card">Patients and<br>caregivers<div class="photo" role="img" aria-label="Portrait of a nurse"></div></div>
    <div class="audience-card">Patients and<br>caregivers<div class="photo" role="img" aria-label="Portrait of a physician"></div></div>
    <div class="audience-card">Scientists and<br>researchers<div class="photo" role="img" aria-label="Portrait of a researcher"></div></div>
  </div>

  <div class="photo what-photo" role="img" aria-label="Doctor reviewing results on a tablet with a patient"></div>
  <div class="what">
    <h2>What We Do</h2>
    <p>Immunotherapies have transformed cancer treatment — but finding the right T cells remains a major bottleneck. Existing methods are slow, expensive, and biased.</p>
    <p>VORENTbio has developed VORENT, a proprietary platform that rapidly identifies antigen-specific T cells — unlocking a faster, more accurate path to personalized and targeted immune therapies.</p>
    <a class="btn btn-grad" href="#">Learn More</a>
  </div>
</section>

<section class="advantage">
  <h2 class="section-title">The VORENT Advantage</h2>
  <div class="adv-grid">
    <div class="adv-card"><div class="adv-icon"><svg width="18" height="18" viewBox="0 0 24 24"><path d="M13 2 4 14h7l-1 8 9-12h-7z" fill="#E54698"/></svg></div><div><h3>Rapid</h3><p>Identify target-reactive T cells in under 48 hours</p><span class="more">Learn More</span></div></div>
    <div class="adv-card"><div class="adv-icon"><svg width="18" height="18" viewBox="0 0 24 24"><circle cx="12" cy="12" r="8" fill="none" stroke="#6B429C" stroke-width="2.5"/><circle cx="12" cy="12" r="3" fill="#6B429C"/></svg></div><div><h3>Unbiased</h3><p>No prior epitope or HLA knowledge required</p><span class="more">Learn More</span></div></div>
    <div class="adv-card"><div class="adv-icon"><svg width="18" height="18" viewBox="0 0 24 24"><path d="M4 20V12M10 20V7M16 20V10M22 20V4" stroke="#0094D4" stroke-width="2.5"/></svg></div><div><h3>Scalable</h3><p>From early discovery to clinical pipelines</p><span class="more">Learn More</span></div></div>
    <div class="adv-card"><div class="adv-icon"><svg width="18" height="18" viewBox="0 0 24 24"><circle cx="12" cy="12" r="9" fill="none" stroke="#00AB8E" stroke-width="2.5"/><path d="M12 7v10M9 10h5" stroke="#00AB8E" stroke-width="2"/></svg></div><div><h3>Cost-Effective</h3><p>Minimal equipment and lower cost per sample</p><span class="more">Learn More</span></div></div>
  </div>
  <div class="center-btn"><a class="btn btn-dark" href="#">View All Advantage</a></div>
</section>

<section class="future">
  <h2 class="section-title">Enabling the Future of Cancer Immunotherapy</h2>
  <div class="future-grid">
    <article class="future-card"><div class="photo" role="img" aria-label="Clinician and patient in a consultation room"></div><h3>Patient-Specific Targeting</h3><p>Match the right T cells to each individual's tumor signature.</p></article>
    <article class="future-card"><div class="photo" role="img" aria-label="Patient entering a medical scanner"></div><h3>TCR Discovery</h3><p>Accelerate the development of engineered cell therapies.</p></article>
    <article class="future-card"><div class="photo" role="img" aria-label="Researchers working in a laboratory"></div><h3>Monitoring &amp; Biomarkers</h3><p>Track immune response dynamics in real time.</p></article>
  </div>
  <div class="center-btn"><a class="btn btn-dark" href="#">View Of Therapy</a></div>
</section>

<section class="built">
  <div class="built-text">
    <h2>Built for Science.<br>Ready for Business.</h2>
    <p>The global market for T cell-based immunotherapies is booming, yet T cell discovery tools haven't kept pace. With early proof-of-concept data and IP pending, VORENTbio is raising seed investment to scale development, validate with clinical collaborators, and bring this transformative platform to market.</p>
    <div class="built-actions">
      <a class="btn btn-grad" href="#">Download Pitch Deck</a>
      <a class="btn btn-ghost" href="#">Schedule a Call</a>
    </div>
  </div>
  <div class="photo built-photo" role="img" aria-label="Scientist working at a laptop in a bright lab"></div>
</section>

<section class="reviews">
  <h2 class="section-title">Customer review</h2>
  <div class="review-grid">
    <figure class="review">
      <svg class="quote" viewBox="0 0 34 26"><path d="M0 26V14C0 6 4 1 12 0v6c-4 1-6 4-6 8h6v12zM20 26V14c0-8 4-13 12-14v6c-4 1-6 4-6 8h6v12z" fill="#A7469A"/></svg>
      <blockquote>"VORENT is a breakthrough in T cell discovery. We've used it to isolate rare tumor-reactive cells we couldn't detect with standard methods."</blockquote>
      <figcaption class="reviewer"><div class="photo" role="img" aria-label="Reviewer portrait"></div><div><div class="stars">★★★★★</div>Dr. Helen Marsh<span>Director of Immuno-Oncology, Northgate Cancer Institute</span></div></figcaption>
    </figure>
    <figure class="review">
      <svg class="quote" viewBox="0 0 34 26"><path d="M0 26V14C0 6 4 1 12 0v6c-4 1-6 4-6 8h6v12zM20 26V14c0-8 4-13 12-14v6c-4 1-6 4-6 8h6v12z" fill="#A7469A"/></svg>
      <blockquote>"The speed and sensitivity of VORENT gives us a clear edge in identifying personalized T cell targets for our clinical pipeline."</blockquote>
      <figcaption class="reviewer"><div class="photo" role="img" aria-label="Reviewer portrait"></div><div><div class="stars">★★★★★</div>Dr. Tomas Lindqvist<span>CSO, Halvern Therapeutics</span></div></figcaption>
    </figure>
  </div>
</section>

<section class="talk">
  <div class="photo talk-photo" role="img" aria-label="Team of doctors and nurses standing together"></div>
  <div class="talk-text">
    <h2>Let's Talk</h2>
    <p>Whether you're an investor, researcher, or strategic partner, we welcome collaboration. Get in touch to learn how VORENTbio can advance your immunotherapy pipeline.</p>
    <a class="btn btn-grad" href="#">Get Started</a>
  </div>
</section>

<footer class="footer">
  <div class="footer-cols">
    <div class="footer-about">
      <a class="brand" href="#"><span class="brand-dot"></span>vorentbio</a>
      <p>VORENTbio developed a platform/technology to identify antigen-specific T cells for cancer therapy, autoimmunity, and more.</p>
    </div>
    <div class="footer-col"><h4>Quick Links</h4><ul><li>Home</li><li>About Us</li><li>Studies</li><li>Careers</li><li>Investors</li></ul></div>
    <div class="footer-col"><h4>Contact Info</h4><ul><li><span class="icon-sq"></span>+1 555 0142</li><li><span class="icon-sq"></span>Boston, MA</li><li><span class="icon-sq"></span>hello@vorentbio.com</li></ul></div>
    <div class="footer-col"><h4>Follow Us</h4><ul><li><span class="icon-sq"></span>Pageboard</li><li><span class="icon-sq"></span>Snapwall</li><li><span class="icon-sq"></span>Chirpline</li></ul></div>
    <div class="footer-col news"><h4>Newsletter Signup</h4><div class="news-form"><span>Enter your email</span><b>Subscribe</b></div></div>
  </div>
  <div class="footer-bar">
    <span>© 2025 VORENTbio. All rights reserved.</span>
    <nav><a href="#">Company</a><a href="#">Privacy Policy</a><a href="#">Terms and Conditions</a></nav>
  </div>
</footer>

</body>
</html>
```